3D Printing Website redesign

We are in the process of redesigning our website. Attached is an image of one of the proposed pages - "The Quotewheel". The idea with this page is that site visitors can get an indicative estimate of the cost of 3D Printing based on some provided metrics. When the user alters the metrics the price changes accordingly. We are looking for a design to support this page that will also be used across our site.

Industry/Entity Type

Printing

```html
<!DOCTYPE html>
<html lang="en">
<head>
<meta charset="utf-8">
<title>The Quotewheel – Layerform Studio</title>
<link href="https://fonts.googleapis.com/css2?family=Lato:wght@300;400;700&display=swap" rel="stylesheet">
<style>
:root{
  --sky:#0aa0e3;
  --sky-dark:#2a7fc0;
  --navy:#2e3d7c;
  --navy-bar:#334285;
  --ink:#3a3a3a;
  --muted:#8a8a8a;
  --page:#f1f1f1;
  --footer:#ebebeb;
  --white:#ffffff;
}
*{box-sizing:border-box;margin:0;padding:0}
html,body{width:1183px;height:1200px;overflow:hidden}
body{position:relative;font-family:'Lato',sans-serif;background:var(--page);color:var(--ink)}
.abs{position:absolute}

.topbar{left:0;top:0;width:1183px;height:47px;background:var(--sky);color:var(--white)}
.topbar .contact{left:190px;top:0;height:47px;display:flex;align-items:center;gap:8px;font-size:14px;white-space:nowrap}
.topbar .auth{right:282px;top:15px;font-size:14.5px;white-space:nowrap}
.topbar .menu-btn{left:915px;top:0;width:46px;height:47px;background:#2a8ad0;display:flex;align-items:center;justify-content:center}
.topbar .search-btn{left:961px;top:0;width:47px;height:47px;background:#3e6fb6;display:flex;align-items:center;justify-content:center}

.navbar{left:0;top:47px;width:1183px;height:74px;background:var(--white);box-shadow:0 2px 6px rgba(0,0,0,.06)}
.brand{left:176px;top:10px;display:flex;align-items:center;gap:10px}
.brand .mark{width:52px;height:52px;border-radius:50%;background:var(--navy)}
.brand .name{font-size:19px;font-weight:700;color:var(--navy)}
.nav{left:395px;top:22px;display:flex;align-items:center;font-size:10.5px;color:var(--muted);white-space:nowrap}
.nav .home{margin-right:10px}
.nav span{padding:0 6px;border-left:1px solid #ccc;line-height:14px}
.nav span:nth-child(2){border-left:none}
.nav .current{color:var(--navy);font-weight:700}

.service{left:180px;width:132px;text-align:center;font-size:16px;color:var(--navy);border-bottom:1px solid #e2e2e2;box-shadow:0 6px 6px -6px rgba(0,0,0,.15)}
.service .art{width:66px;height:66px;margin:0 auto 8px;background:linear-gradient(135deg,#7ccbf0,#1f86c8);border-radius:4px}
.divider{left:312px;top:160px;width:1px;height:340px;background:linear-gradient(#ddd,transparent)}

.quote-title{left:330px;top:139px;width:464px;text-align:center;font-size:24px;font-weight:700;color:var(--navy)}
.quote-or{left:330px;top:168px;width:464px;text-align:center;font-size:24px;font-weight:300;color:var(--navy)}
.label{width:320px;text-align:center;font-size:14px;font-weight:700;color:#444}
.slider{width:313px;height:6px;background:#d8d8d8;border:1px solid #bdbdbd;border-radius:1px}
.slider .knob{position:absolute;top:-12px;width:14px;height:28px;background:var(--sky)}
.side{font-size:14px;color:var(--muted)}
.select{left:408px;top:440px;width:312px;height:40px;background:#dcdcdc;border:1px solid #bdbdbd}
.select .caret{position:absolute;right:0;top:0;width:46px;height:38px;border-left:1px solid #bdbdbd;background:#d0d0d0;display:flex;align-items:center;justify-content:center}
.preview{left:806px;top:237px;width:188px;height:188px;border-radius:50%;background:#9fd3f1;border:1px solid #8cc6e8}
.total{left:780px;top:451px;width:240px;text-align:center;font-size:14px;font-weight:700;color:#333}

.intro{left:0;top:520px;width:1173px;text-align:center;font-size:18.5px;font-weight:300;color:#777}
.field{width:378px;height:39px;background:var(--white);border:1px solid #ccc;font-size:12.5px;color:#555;padding:12px 9px}
.captcha-note{left:624px;top:593px;font-size:12.8px;color:#555}
.captcha{left:618px;top:636px;width:190px;height:58px;background:var(--white);padding:5px 7px}
.captcha .img{width:100%;height:100%;background:linear-gradient(90deg,#c9d3e6,#aeb9d6);border:1px solid #999}
.captcha-tools{left:817px;top:658px;display:flex;gap:10px;align-items:center}
.check{left:621px;top:784px;display:flex;align-items:center;gap:10px;font-size:13.8px;color:#333}
.check .box{width:20px;height:20px;border:1px solid #aaa;background:#f5f5f5}
.submit{left:619px;top:837px;width:378px;height:39px;border:1px solid var(--sky);background:var(--white);color:var(--sky);font-size:14px;text-align:center;line-height:37px}
.footnote{left:219px;top:913px;font-size:11.2px;color:#555}

.footer{left:0;top:953px;width:1183px;height:199px;background:var(--footer)}
.fcol{font-size:10.5px;color:#666;line-height:15.6px}
.fcol b{color:var(--navy);font-weight:700;display:block}
.fcol .gap{height:15px}
.news-title{left:675px;top:981px;font-size:23px;font-weight:700;color:var(--navy)}
.news-sub{left:677px;top:1006px;font-size:21.3px;font-weight:300;color:#555}
.news-input{left:673px;top:1055px;width:303px;height:37px;background:var(--white);border:1px solid #ccc;font-size:13px;color:#999;padding:10px 17px}
.news-input svg{position:absolute;right:10px;top:7px}
.follow{left:674px;top:1113px;font-size:14px;font-weight:700;color:#555}
.social{width:36px;height:36px;border-radius:50%}
.bottombar{left:0;top:1152px;width:1183px;height:48px;background:var(--navy-bar);color:#e8eaf3;font-size:10.5px;text-align:center;line-height:46px}
</style>
</head>
<body>

<header class="abs topbar">
  <div class="abs contact">
    <svg width="24" height="24" viewBox="0 0 24 24" fill="none" stroke="#fff" stroke-width="2"><path d="M6 3l3 4-2 2c1 3 3 5 6 6l2-2 4 3-2 3C10 19 5 14 4 5z"/><path d="M15 4a5 5 0 0 1 5 5M15 1a8 8 0 0 1 8 8"/></svg>
    <span>61 2 5550 1842 | 0400 555 272 | UAN 555-010-333 | Australia</span>
  </div>
  <div class="abs auth">LOG IN | REGISTER</div>
  <div class="abs menu-btn"><svg width="22" height="18"><rect y="1" width="22" height="3" fill="#fff"/><rect y="8" width="22" height="3" fill="#fff"/><rect y="15" width="22" height="3" fill="#fff"/></svg></div>
  <div class="abs search-btn"><svg width="24" height="24" fill="none" stroke="#fff" stroke-width="2.5"><circle cx="14" cy="9" r="7"/><path d="M9 14l-7 7"/></svg></div>
</header>

<nav class="abs navbar">
  <div class="abs brand"><div class="mark"></div><div class="name">Layerform Studio</div></div>
  <div class="abs nav" style="left:395px">
    <svg class="home" width="24" height="22" viewBox="0 0 24 22"><path d="M12 1L1 11h3v10h6v-6h4v6h6V11h3z" fill="var(--sky-dark)"/></svg>
    <span>SHOP</span><span>WHAT WE DO</span><span class="current">THE QUOTEWHEEL</span><span>MATERIALS</span><span>GALLERY</span><span>DIY</span><span>TRAINING</span><span>ABOUT US</span><span>BLOG</span>
  </div>
</nav>

<aside>
  <div class="abs service" style="top:174px;height:98px"><div class="art" role="img" aria-label="Illustration of a 3D printer"></div>PRINT</div>
  <div class="abs service" style="top:290px;height:92px"><div class="art" role="img" aria-label="Illustration of a 3D scanner"></div>SCAN</div>
  <div class="abs service" style="top:396px;height:94px"><div class="art" role="img" aria-label="Illustration of a design blueprint"></div>DESIGN</div>
</aside>
<div class="abs divider"></div>

<h1 class="abs quote-title">GET AN INSTANT QUOTE</h1>
<div class="abs quote-or">OR</div>

<div class="abs label" style="left:403px;top:208px">SHAPE</div>
<div class="abs side" style="left:342px;top:235px">SQUARE</div>
<div class="abs side" style="left:729px;top:236px">CIRCULAR</div>
<div class="abs slider" style="left:406px;top:241px"><div class="knob" style="left:37px"></div></div>

<div class="abs label" style="left:403px;top:280px">SIZE</div>
<div class="abs slider" style="left:406px;top:313px"><div class="knob" style="left:37px"></div></div>

<div class="abs label" style="left:404px;top:352px">VOLUME</div>
<div class="abs slider" style="left:406px;top:378px"><div class="knob" style="left:38px"></div></div>

<div class="abs label" style="left:404px;top:416px">MATERIAL</div>
<div class="abs select"><div class="caret"><svg width="10" height="8"><path d="M0 0h10L5 8z" fill="#444"/></svg></div></div>

<div class="abs preview" role="img" aria-label="Preview of the printed shape"></div>
<div class="abs total">QUOTEWHEEL TOTAL: $36*</div>

<p class="abs intro">For Further information and inquiries, Please fill in the form below:</p>

<div class="abs field" style="left:215px;top:598px">NAME</div>
<div class="abs field" style="left:215px;top:655px">EMAIL</div>
<div class="abs field" style="left:215px;top:712px">PHONE</div>
<div class="abs field" style="left:215px;top:770px;height:106px">INSTRUCTIONS</div>

<p class="abs captcha-note">Please enter the following text to the box below to continue.</p>
<div class="abs captcha"><div class="img" role="img" aria-label="Distorted verification text"></div></div>
<div class="abs captcha-tools">
  <svg width="14" height="14" fill="none" stroke="#555" stroke-width="2"><path d="M12 7a5 5 0 1 1-2-4"/><path d="M10 0v4h3"/></svg>
  <svg width="14" height="14"><path d="M1 5h3l4-4v12L4 9H1z" fill="#555"/><path d="M10 4a4 4 0 0 1 0 6" stroke="#555" fill="none" stroke-width="1.5"/></svg>
  <svg width="14" height="14"><rect width="14" height="14" fill="#555"/><text x="7" y="11" fill="#fff" font-size="10" text-anchor="middle" font-family="Lato,sans-serif" font-weight="700">?</text></svg>
</div>
<div class="abs field" style="left:621px;top:712px;height:39px"></div>
<label class="abs check"><span class="box"></span>I would like to receive promotional material</label>
<div class="abs submit">SUBMIT</div>
<p class="abs footnote">* Duis sed odio sit amet nibh vulputate cursus a sit amet mauris. Morbi accumsan ipsu velitincidunt auctor a orn.</p>

<footer class="abs footer">
  <div class="abs fcol" style="left:178px;top:29px"><b>Printing</b>Quote<br>Technologies<div class="gap"></div><b>Printers</b>Machines for sale<br>Machines to rent<br>Servicing<br>Buy Materials</div>
  <div class="abs fcol" style="left:322px;top:29px"><b>Materials</b>Overview<br>Plastic<br>Powder<br>High-Detail Resin<br>Nylon<br>Wood<br>Rubber</div>
  <div class="abs fcol" style="left:475px;top:29px"><b>Training</b>Harbour 3D Makers<br>Meetup<br>Studio Workshops<div class="gap"></div><b>Franchise</b>Franchise Opportunity</div>
</footer>
<h2 class="abs news-title">Newsletter</h2>
<div class="abs news-sub">Want to receive our Newsletter?</div>
<div class="abs news-input">ENTER YOUR EMAIL
  <svg width="44" height="22" fill="none" stroke="#444" stroke-width="1.5"><path d="M0 3h10M4 7h8M8 11h6"/><rect x="16" y="2" width="26" height="18"/><path d="M16 2l13 10 13-10"/></svg>
</div>
<div class="abs follow">Follow Us</div>
<div class="abs social" style="left:899px;top:1103px;background:var(--navy)"></div>
<div class="abs social" style="left:939px;top:1103px;background:var(--sky)"></div>

<div class="abs bottombar">COPYRIGHT © 2014 LAYERFORM STUDIO &nbsp;&nbsp;&nbsp;|&nbsp;&nbsp;&nbsp; ALL RIGHTS RESERVED</div>

</body>
</html>
```